Camp Thornbrook 2021 Magazine Design

We are for someone to design our annual magazine/newsletter. This is a print newsletter that is a total of 20 pages. It will need to be designed in a way that is easy to share with our printers. The designer will need to be someone who is creative and easy to work with.
For those interested in this project we ask that you design 4 to 6 pages for us to view. Once we select the designer we will want the rest created in a two-week time span. For those submitting a bid please include front cover, theme & dates, mission & vision, and Lend a Hand Forward.

This link will provide the layout of the newsletter https://files.pelmarsh.example/doc/7qTzR2kLpW9xVbN4cHsYd/view.

This link will provide you with the pictures that are needed and a few documents https://files.pelmarsh.example/folder/3hGvK8mQxZ5rLtP1wNcBj/view

Details:
20 pages long (including covers)
8.5 x 11

Please message me if you need any further details.

Target Market(s)

Our alumni base. Covers all ages

Requirements
Must have
• Spelled out in document
Nice to have
• Spelled out in document
Should not have
• Spelled out in document

```html
<!DOCTYPE html>
<html lang="en">
<head>
<meta charset="utf-8">
<title>Camp Thornbrook 2021 — Spread</title>
<link href="https://fonts.googleapis.com/css2?family=Roboto+Slab:wght@800;900&family=Roboto:wght@500&display=swap" rel="stylesheet">
<style>
  :root {
    --backdrop: #ecece8;
    --page-light: #d8dad3;
    --year-ink: #5c665f;
    --forest-dark: #2a372d;
    --forest-mid: #3c5a3a;
    --frame-line: #d9dcd6;
    --toc-ink: #d3d6d0;
    --title-ink: #e4e6e1;
  }
  * { margin: 0; padding: 0; box-sizing: border-box; }
  html, body {
    width: 1200px; height: 900px; overflow: hidden;
    background: var(--backdrop);
  }
  .spread {
    position: absolute; left: 40px; top: 50px;
    width: 1120px; height: 800px;
    display: flex;
    box-shadow: 0 10px 30px rgba(0,0,0,0.18);
  }
  .page { position: relative; width: 560px; height: 800px; overflow: hidden; }

  /* Left page: cover */
  .page--cover {
    background: linear-gradient(90deg, #e1e3dc 0%, var(--page-light) 85%, #c6c9c1 100%);
  }
  .cover-photo {
    position: absolute; left: 126px; top: 156px; width: 310px; height: 427px;
    background:
      linear-gradient(180deg,
        #c8703c 0%, #c8703c 25%,
        #3f4437 25%, #3f4437 50%,
        #e0a43a 50%, #e0a43a 75%,
        #9cb6d6 75%, #9cb6d6 100%);
  }
  .cover-photo::after {
    content: ""; position: absolute; left: 50%; top: 0; width: 50%; height: 100%;
    background: linear-gradient(180deg,
        #3e7a44 0%, #3e7a44 25%,
        #e8b487 25%, #e8b487 50%,
        #3a3d55 50%, #3a3d55 75%,
        #e8cd3a 75%, #e8cd3a 100%);
  }
  .cover-year {
    position: absolute; left: 122px; top: 578px; width: 318px;
    font-family: "Roboto Slab", serif; font-weight: 900;
    font-size: 123px; line-height: 1; letter-spacing: 2px;
    color: var(--year-ink); text-align: center;
  }

  /* Right page: contents */
  .page--contents { background: var(--forest-dark); }
  .contents-photo {
    position: absolute; left: 0; top: 0; width: 188px; height: 800px;
    background: linear-gradient(90deg, #5f7a4c 0%, #6b6452 45%, #4d4a40 75%, #3e3f35 100%);
  }
  .contents-shade {
    position: absolute; left: 188px; top: 0; width: 372px; height: 800px;
    background: linear-gradient(180deg, #2d3b30 0%, var(--forest-dark) 100%);
  }
  .contents-frame { position: absolute; left: 0; top: 0; }
  .contents-title {
    position: absolute; left: 355px; top: 424px;
    font-family: "Roboto Slab", serif; font-weight: 800;
    font-size: 32px; line-height: 34px; color: var(--title-ink);
  }
  .contents-list {
    position: absolute; left: 271px; top: 609px; width: 260px;
    list-style: none;
    font-family: "Roboto", sans-serif; font-weight: 500;
    font-size: 9.5px; line-height: 13.4px; color: var(--toc-ink);
  }
  .contents-list li { display: flex; }
  .contents-list .entry { width: 149px; }
</style>
</head>
<body>
  <main class="spread">
    <section class="page page--cover">
      <div class="cover-photo" role="img" aria-label="Photo of colourful signed camp plaques from past summers"></div>
      <div class="cover-year">2021</div>
    </section>

    <section class="page page--contents">
      <div class="contents-photo" role="img" aria-label="Photo of a carved tree stump at camp with woods behind"></div>
      <div class="contents-shade"></div>
      <svg class="contents-frame" width="560" height="800" viewBox="0 0 560 800" aria-hidden="true">
        <path d="M466 412 V308 H271 V577 H466 V509" fill="none" stroke="var(--frame-line)" stroke-width="1.6"/>
      </svg>
      <h1 class="contents-title">Table of<br>Contents</h1>
      <ul class="contents-list">
        <li><span class="entry">Lend a Hand Forward</span><span>Page 3</span></li>
        <li><span class="entry">Golf Tournament</span><span>Pages 4 &amp; 5</span></li>
        <li><span class="entry">2021 Theme and Dates</span><span>Pages 6 &amp; 7</span></li>
        <li><span class="entry">Where Are They Now: Dale Hollis</span><span>Pages 8 &amp; 9</span></li>
        <li><span class="entry">2019 Donors</span><span>Pages 10, 11, &amp; 12</span></li>
        <li><span class="entry">2019 Thornbrook Awards</span><span>Page 13</span></li>
        <li><span class="entry">Bee Rock</span><span>Pages 14 &amp;15</span></li>
        <li><span class="entry">Mission/Vision</span><span>Pages 16 &amp; 17</span></li>
        <li><span class="entry">A Place We Call Home</span><span>Page 18</span></li>
        <li><span class="entry">Memorials</span><span>Page 19</span></li>
      </ul>
    </section>
  </main>
</body>
</html>
```